Business Cards Needed For Veterinary Business

Looking for a business card design for a veterinary blood bank. We would like it to be clean and professional on appearance but still warm and inviting. We would like to utilize our logo and similar coloring. We will use our phone number, email, website, employee name, employee title.

We do not want a bunch of animated animal photos but do not need the style to be as clinical as a laboratory or human medical procedure office.

We are looking for some creative ideas to choose from so that we can generate a standout professional business card for our management team to utilize.

Target Market(s)

professionals

Industry/Entity Type

veterinary

Contact Information for Business Card

employee name, employee title, phone number, website URL, email

Font styles to use
Sans Serif

Colors
0054AA
0677BA
7BADD7
CADEEF
E8F1F8
EB3D1F
EC4F4E
F09395
F8D3D4
FCEDEE

Requirements
Nice to have
• creative design
Should not have
• animated photos

```html
<!DOCTYPE html>
<html lang="en">
<head>
<meta charset="utf-8">
<title>Lumen Vet Bank — Business Card</title>
<link href="https://fonts.googleapis.com/css2?family=Montserrat:wght@400;500;800;900&display=swap" rel="stylesheet">
<style>
  :root{
    --bg:#d3d3cf;
    --card-black:#1b1b1c;
    --gloss-dark:#151516;
    --gloss-light:#4a4a4c;
    --red:#eb1c24;
    --white:#ffffff;
    --soft-white:#e9e9e9;
  }
  *{margin:0;padding:0;box-sizing:border-box}
  html,body{width:1200px;height:801px;overflow:hidden;background:var(--bg);font-family:"Montserrat",sans-serif}
  .stage{position:relative;width:1200px;height:801px}
  .card{position:absolute;top:246px;width:540px;height:309px;background:var(--card-black);
        border-bottom:4px solid var(--red);overflow:hidden;box-shadow:0 14px 28px rgba(0,0,0,.28)}
  .card--front{left:40px}
  .card--back{left:620px}

  .front-corner{position:absolute;inset:0}
  .brand{position:absolute;display:flex;align-items:center;gap:10px}
  .brand__dot{width:30px;height:30px;border-radius:50%;background:var(--red);flex:none}
  .brand__name{color:var(--red);font-weight:900;font-size:24px;letter-spacing:.5px;line-height:1;text-transform:uppercase}
  .card--front .brand{left:34px;top:46px}

  .person{position:absolute;left:34px;top:150px}
  .person__name{color:var(--red);font-weight:900;font-size:24px;text-transform:uppercase;letter-spacing:.5px}
  .person__title{color:var(--white);font-weight:500;font-size:14px;margin-top:4px}

  .contacts{position:absolute;left:34px;top:222px;list-style:none}
  .contacts li{display:flex;align-items:center;gap:8px;color:var(--white);font-size:13px;font-weight:400;line-height:22px}
  .contacts svg{width:12px;height:12px;flex:none}

  .gloss{position:absolute;inset:0;background:linear-gradient(200deg,var(--gloss-light) 0%,#2e2e30 30%,var(--gloss-dark) 60%,var(--gloss-dark) 100%)}
  .card--back .brand{right:40px;top:138px}
</style>
</head>
<body>
<main class="stage">

  <section class="card card--front">
    <svg class="front-corner" viewBox="0 0 540 309" aria-hidden="true">
      <polygon points="300,0 540,0 540,205" fill="var(--white)"/>
      <line x1="300" y1="0" x2="540" y2="205" stroke="var(--red)" stroke-width="3"/>
    </svg>

    <div class="brand">
      <span class="brand__dot"></span>
      <span class="brand__name">Lumen Vet Bank</span>
    </div>

    <div class="person">
      <h1 class="person__name">Dana Mercer</h1>
      <p class="person__title">Director</p>
    </div>

    <ul class="contacts">
      <li>
        <svg viewBox="0 0 24 24"><path fill="var(--red)" d="M6.6 10.8a15 15 0 0 0 6.6 6.6l2.2-2.2a1 1 0 0 1 1-.25 11.4 11.4 0 0 0 3.6.57 1 1 0 0 1 1 1V20a1 1 0 0 1-1 1A17 17 0 0 1 3 4a1 1 0 0 1 1-1h3.5a1 1 0 0 1 1 1c0 1.25.2 2.45.57 3.57a1 1 0 0 1-.25 1z"/></svg>
        555.204.7731
      </li>
      <li>
        <svg viewBox="0 0 24 24"><rect x="2" y="5" width="20" height="14" fill="none" stroke="var(--red)" stroke-width="2"/><path d="M2 5l10 8 10-8" fill="none" stroke="var(--red)" stroke-width="2"/></svg>
        hello@lumenvetbank.com
      </li>
      <li>
        <svg viewBox="0 0 24 24"><circle cx="12" cy="12" r="10" fill="var(--red)"/><path d="M2 12h20M12 2c3 3 3 17 0 20M12 2c-3 3-3 17 0 20" fill="none" stroke="var(--card-black)" stroke-width="1.5"/></svg>
        www.lumenvetbank.com
      </li>
    </ul>
  </section>

  <section class="card card--back">
    <div class="gloss" role="img" aria-label="Glossy black surface with a tone-on-tone repeat pattern"></div>
    <div class="brand">
      <span class="brand__dot"></span>
      <span class="brand__name">Lumen Vet Bank</span>
    </div>
  </section>

</main>
</body>
</html>
```